Vesit cards for web development company

We need a business card design for our company. The company develops online platforms and conducts marketing consulting. Company logo. The cards must fit in with us (a junior start UP), but they must also be professional enough to impress with investors like banks. We wish you a combination of classic and modern design

Target Market(s)

Business partners and IT and marketing customers

Industry/Entity Type

It Company

Contact Information for Business Card

Folgende Information müssen Drauf.
Name, Position, Telefon Nr., Mobile Nr., E-Mail adresse, Optional sind noch Webadresse und HRB Nummer

Colors

Designer to choose colors to be used in the design.

Requirements
Must have
• The cards have to fit into the logo later and have to be dynamic and serious at the same time

```html
<!DOCTYPE html>
<html lang="en">
<head>
<meta charset="utf-8">
<title>Orvanta Development – Business Card</title>
<link rel="stylesheet" href="https://fonts.googleapis.com/css2?family=Open+Sans:wght@400;700;800&family=Tinos&display=swap">
<style>
  :root {
    --page-bg: #3a3431;
    --card-bg: #121314;
    --brand-blue: #1f7fc8;
    --text-white: #f2f2f2;
    --text-grey: #9a9a9a;
    --divider: #8a8a8a;
  }
  * { box-sizing: border-box; margin: 0; padding: 0; }
  html, body { width: 1200px; height: 864px; overflow: hidden; }
  body {
    background: var(--page-bg);
    display: flex;
    align-items: center;
    justify-content: center;
    gap: 48px;
    font-family: "Open Sans", Arial, sans-serif;
  }
  .card {
    width: 540px;
    height: 309px;
    background: var(--card-bg);
    border-radius: 3px;
    box-shadow: 0 10px 28px rgba(0,0,0,0.45);
    position: relative;
    color: var(--text-white);
  }
  .brand-name {
    font-family: "Open Sans", Arial, sans-serif;
    font-weight: 800;
    color: var(--brand-blue);
    text-transform: uppercase;
    line-height: 1.05;
    text-align: center;
    letter-spacing: 0.5px;
  }
  /* Front */
  .card-front {
    display: flex;
    flex-direction: column;
    align-items: center;
    justify-content: center;
  }
  .card-front .brand-name { font-size: 40px; }
  .card-front .website {
    margin-top: 22px;
    font-size: 14px;
    letter-spacing: 5px;
    color: var(--text-grey);
  }
  /* Back */
  .card-back .brand-name {
    position: absolute;
    top: 70px; left: 0; right: 0;
    font-size: 34px;
  }
  .card-back .details {
    position: absolute;
    top: 168px; left: 0; right: 0;
    display: flex;
    justify-content: center;
  }
  .identity {
    text-align: right;
    padding-right: 18px;
    padding-top: 6px;
  }
  .person-name {
    font-weight: 700;
    font-size: 14px;
    color: var(--brand-blue);
    text-transform: uppercase;
  }
  .person-role {
    font-size: 15px;
    text-transform: uppercase;
    color: var(--text-white);
  }
  .divider {
    width: 1px;
    height: 72px;
    background: var(--divider);
  }
  .contacts {
    list-style: none;
    padding-left: 18px;
    font-family: "Tinos", "Times New Roman", serif;
    font-size: 15px;
    line-height: 19px;
  }
  .contacts li { display: flex; align-items: center; gap: 9px; }
  .contacts svg { width: 11px; height: 11px; fill: var(--brand-blue); flex: none; }
</style>
</head>
<body>
  <section class="card card-front">
    <div class="brand-name">Orvanta<br>Development</div>
    <div class="website">www.orvantadev.com</div>
  </section>

  <section class="card card-back">
    <div class="brand-name">Orvanta Development</div>
    <div class="details">
      <div class="identity">
        <div class="person-name">Mark Keller</div>
        <div class="person-role">CEO/Founder</div>
      </div>
      <div class="divider"></div>
      <ul class="contacts">
        <li>
          <svg viewBox="0 0 12 12" aria-hidden="true"><path d="M2 1h2.5l1 3-1.5 1a6 6 0 0 0 3 3l1-1.5 3 1V10a1.5 1.5 0 0 1-1.5 1.5A9.5 9.5 0 0 1 .5 2.5 1.5 1.5 0 0 1 2 1z"/></svg>
          555 014 2281
        </li>
        <li>
          <svg viewBox="0 0 12 12" aria-hidden="true"><path d="M3 0h6a1 1 0 0 1 1 1v10a1 1 0 0 1-1 1H3a1 1 0 0 1-1-1V1a1 1 0 0 1 1-1zm0.5 1.5v8h5v-8z"/></svg>
          555 019 7730
        </li>
        <li>
          <svg viewBox="0 0 12 12" aria-hidden="true"><path d="M0 2h12v8H0zm1 1v.4l5 3.2 5-3.2V3z"/></svg>
          mark@orvantadev.com
        </li>
        <li>
          <svg viewBox="0 0 12 12" aria-hidden="true"><path d="M6 0a6 6 0 1 0 0 12A6 6 0 0 0 6 0zm0 1.2c.7.7 1.2 2 1.4 3.6H4.6C4.8 3.2 5.3 1.9 6 1.2zM1.3 5.8h2.3c0 1.3.3 2.6.8 3.6a4.8 4.8 0 0 1-3.1-3.6zm3.3 0h2.8c-.1 1.6-.6 3-1.4 3.9-.8-.9-1.3-2.3-1.4-3.9zm3.8 0h2.3a4.8 4.8 0 0 1-3.1 3.6c.5-1 .8-2.3.8-3.6z"/></svg>
          www.orvantadev.com
        </li>
      </ul>
    </div>
  </section>
</body>
</html>
```